Animal Feed Bag Packaging Design

The task is to design a livestock feed bag. These are 18"x32" and typically hold 50 LBS of feed. This design will be on all of the packaging for our feed bags. These feed bags will be sold in local feed and hardware stores and will hold a variety of different feed products for all classes of livestock. The bags will be double sided. I would like the back side to remain consistent, but I would like the front of the bag to have 4 different varieties that share the same layout, but incorporate different titles and possible graphics. The Categories will be:
- "Poultry Feed" This will be for all classes of poultry
- "Hog Feed" This will be for all classes of hogs
- "Mixed Feed" This will be a sort of catch all design that will be used for a variety of different types of livestock feed (cows, goats, sheep, rabbits)
- "Feed & Grain": This will also be a miscelaneous category that will be used for whole grains and feeds that can be used across multiple animal types.

I have attached many photos that may or may not be used, but that may help to portray our operation and what we do.

Target Market(s)

Backyard Hobby Farmers and Livestock Enthusists

Industry/Entity Type

Agriculture

Font styles to use
Serif

Colors

Designer to choose colors to be used in the design.

Requirements
Must have
• Must contain our logo and have a strong brand presence for "Harlow Kin's Feed". Each bag needs to contain the the following on either the front or backside of the bag. Harlow Kin's Feed - 218 West Orchard Lane Brackton Utah, 84621 - 435 712 0968 - harlowkinsfeed.example
Nice to have
• Our brand is built around these factors that could be incorporated into the design: Locally Milled, Quality Ingredients, Balanced Nutrition, Family Owned & Operated Est. 2017. Home delivery is also a core competency of our operation. I will attach a few images of our farm where we operate at that may be incorporated if it fits the style.

```html
<!DOCTYPE html>
<html lang="en">
<head>
<meta charset="utf-8">
<title>Harlow Kin's Feed – Hog Feed Bag</title>
<link href="https://fonts.googleapis.com/css2?family=Archivo+Black&family=Montserrat:wght@400;600;700&display=swap" rel="stylesheet">
<style>
  :root {
    --purple: #6f2c91;
    --purple-dark: #5a2277;
    --tan: #f3cf96;
    --bag: #f4f4f2;
    --ink: #2a2a2a;
    --stage: #cfcfcf;
  }
  html, body { margin: 0; padding: 0; overflow: hidden; }
  body { width: 1200px; height: 2593px; background: var(--stage); position: relative; font-family: "Montserrat", sans-serif; color: var(--ink); }
  .shapes { position: absolute; left: 0; top: 0; }
  .t { position: absolute; margin: 0; text-align: center; }
  .heavy { font-family: "Archivo Black", sans-serif; }
  .tag-note { left: 290px; width: 616px; top: 140px; font-size: 12px; font-weight: 700; letter-spacing: .2px; }
  .brand-name { font-family: "Archivo Black", sans-serif; color: #fff; font-size: 14px; letter-spacing: 1px; width: 230px; }
  .kicker { left: 330px; width: 535px; top: 862px; font-family: "Archivo Black", sans-serif; color: #fff; font-size: 22px; letter-spacing: 5px; }
  .product-title { left: 330px; width: 535px; top: 890px; font-family: "Archivo Black", sans-serif; color: #fff; font-size: 80px; line-height: 1; letter-spacing: -1px; }
  .feature { position: absolute; font-family: "Archivo Black", sans-serif; font-size: 15px; line-height: 17px; letter-spacing: .5px; text-align: left; margin: 0; }
  .weight { left: 515px; width: 170px; top: 1035px; font-family: "Archivo Black", sans-serif; color: var(--purple); font-size: 104px; line-height: 1; letter-spacing: -4px; }
  .weight-unit { left: 515px; width: 170px; top: 1140px; font-family: "Archivo Black", sans-serif; color: var(--purple); font-size: 28px; }
  .story { left: 330px; width: 540px; top: 1688px; font-size: 15.5px; line-height: 24px; text-transform: uppercase; }
  .story .brand { color: var(--purple); font-weight: 700; }
  .service h3 { margin: 0; font-family: "Archivo Black", sans-serif; color: var(--purple); font-size: 21px; line-height: 23px; letter-spacing: .5px; }
  .service p { margin: 6px 0 0; font-size: 12px; font-weight: 600; line-height: 16px; }
  .contact { position: absolute; left: 508px; margin: 0; font-size: 15px; font-weight: 700; line-height: 19px; }
</style>
</head>
<body>
<svg class="shapes" width="1200" height="2593" viewBox="0 0 1200 2593">
  <defs>
    <linearGradient id="photo-hog" x1="0" y1="0" x2="0" y2="1">
      <stop offset="0" stop-color="#e9b08a"/><stop offset=".6" stop-color="#d68c67"/><stop offset="1" stop-color="#6e3b22"/>
    </linearGradient>
  </defs>

  <!-- front bag -->
  <rect x="290" y="90" width="600" height="1128" rx="14" fill="var(--bag)"/>
  <rect x="292" y="264" width="594" height="16" fill="var(--tan)"/>
  <rect x="292" y="280" width="594" height="54" fill="var(--purple)"/>
  <rect x="290" y="310" width="600" height="542" fill="url(#photo-hog)" role="img" aria-label="Photo of a young piglet looking at the camera among other pigs"/>
  <rect x="286" y="850" width="608" height="40" fill="var(--purple)"/>
  <rect x="286" y="890" width="608" height="30" fill="var(--tan)"/>
  <rect x="330" y="835" width="535" height="180" rx="22" fill="var(--purple)"/>
  <line x1="372" y1="880" x2="436" y2="880" stroke="var(--tan)" stroke-width="2"/>
  <line x1="757" y1="880" x2="821" y2="880" stroke="var(--tan)" stroke-width="2"/>
  <circle cx="598" cy="287" r="117" fill="var(--purple)"/>
  <circle cx="598" cy="240" r="22" fill="none" stroke="#fff" stroke-width="3"/>

  <g fill="var(--purple)">
    <circle cx="353" cy="1062" r="7"/><circle cx="353" cy="1110" r="7"/>
    <circle cx="696" cy="1056" r="7"/><circle cx="696" cy="1104" r="7"/>
  </g>
  <g fill="none" stroke="#fff" stroke-width="2" stroke-linecap="round">
    <path d="M350 1062l2.5 2.5 4-5"/><path d="M350 1110l2.5 2.5 4-5"/>
    <path d="M693 1056l2.5 2.5 4-5"/><path d="M693 1104l2.5 2.5 4-5"/>
  </g>

  <!-- back bag -->
  <rect x="290" y="1350" width="600" height="1120" rx="14" fill="var(--bag)"/>
  <rect x="292" y="1522" width="594" height="16" fill="var(--tan)"/>
  <rect x="292" y="1538" width="594" height="56" fill="var(--purple)"/>
  <circle cx="598" cy="1544" r="117" fill="var(--purple)"/>
  <circle cx="598" cy="1497" r="22" fill="none" stroke="#fff" stroke-width="3"/>

  <circle cx="403" cy="2005" r="95" fill="#7f9a6a" stroke="var(--purple)" stroke-width="4" role="img" aria-label="Photo of a delivery truck with feed totes in a green field"/>
  <circle cx="598" cy="2005" r="95" fill="#a07a52" stroke="var(--purple)" stroke-width="4" role="img" aria-label="Photo of cupped hands holding mixed grain feed"/>
  <circle cx="790" cy="2005" r="95" fill="#6f89a6" stroke="var(--purple)" stroke-width="4" role="img" aria-label="Photo of feed sacks beside blue barrels"/>

  <line x1="327" y1="2242" x2="866" y2="2242" stroke="var(--purple)" stroke-width="1.5"/>
  <g fill="var(--purple)">
    <path d="M478 2276a7 7 0 0 1 7 7c0 6-7 12-7 12s-7-6-7-12a7 7 0 0 1 7-7z"/>
    <circle cx="478" cy="2359" r="8"/>
    <circle cx="478" cy="2395" r="8"/>
  </g>
  <circle cx="478" cy="2283" r="2.5" fill="#fff"/>
  <path d="M474.5 2355c1 3 3 5.5 6.5 7l1.5-1.8-2-1.3-1 1c-1.3-.6-2.3-1.6-3-3l1-1-1.2-2z" fill="#fff"/>
  <g fill="none" stroke="#fff" stroke-width="1.3">
    <circle cx="478" cy="2395" r="5"/><ellipse cx="478" cy="2395" rx="2" ry="5"/><line x1="473" y1="2395" x2="483" y2="2395"/>
  </g>
</svg>

<!-- front -->
<p class="t tag-note">SEE ATTACHED TAG FOR SPECIFIC FEED INFORMATION</p>
<p class="t brand-name" style="left:483px;top:292px;">HARLOW KIN'S FEED</p>
<p class="t kicker">LOCALLY MILLED</p>
<h1 class="t product-title">HOG FEED</h1>
<p class="feature" style="left:374px;top:1052px;">HOME<br>DELIVERY</p>
<p class="feature" style="left:374px;top:1101px;">QUALITY<br>INGREDIENTS</p>
<p class="feature" style="left:717px;top:1046px;">BALANCED<br>NUTRITION</p>
<p class="feature" style="left:717px;top:1094px;">FAMILY OWNED<br>&amp; OPERATED</p>
<p class="t weight">50</p>
<p class="t weight-unit">LBS</p>

<!-- back -->
<p class="t brand-name" style="left:483px;top:1549px;">HARLOW KIN'S FEED</p>
<p class="t story"><span class="brand">Harlow Kin's Feed</span> is owned and operated by brothers–Wade and Ellis–and proudly located in the small town of Brackton, Utah. For over 10 years, we've crafted premium feed with the highest quality ingredients because we know what it takes to raise healthy animals. As lifelong farmers and ranchers, we're proud to serve your operation with honesty, integrity, and a true commitment to quality.</p>

<div class="t service" style="left:318px;width:170px;top:2122px;"><h3>HOME<br>DELIVERY</h3><p>FROM OUR MILL TO<br>YOUR GATE,<br>HASSLE FREE</p></div>
<div class="t service" style="left:513px;width:170px;top:2120px;"><h3>LOCALLY<br>MILLED</h3><p>MIXED DAILY AND<br>GUARANTEED FRESH</p></div>
<div class="t service" style="left:695px;width:190px;top:2116px;"><h3>BULK<br>QUANTITIES</h3><p>FROM BARRELS TO TOTES,<br>SIZED TO FIT YOUR<br>OPERATION</p></div>

<p class="contact" style="top:2272px;">HARLOW KIN'S FEED<br>218 WEST ORCHARD LANE<br>BRACKTON, UTAH 84621</p>
<p class="contact" style="top:2349px;">(435) 712-0968</p>
<p class="contact" style="top:2385px;">HARLOWKINSFEED.EXAMPLE</p>
</body>
</html>
```